Poster for teenagers

Bright, trendy, modern and young fonts - a variety of fonts, plus arrows and clip art (no photos) for an A3 size poster to be hung in study halls of schools. There are six dot points. I think each point should be in some kind of box or circle.

Here are a few ideas of the kind of thing I mean.
http://www.varrowdale.example.gov.au/Page/Images/youth_Advisory_Group_Poster_(1).jpg

http://www.brindlecourt.example/sites/default/files/Youth-Panel-Poster-1-Web.jpg

http://www.quillmarsh.example.org.au/images/librariesprovider4/Misc-illustrations/140335-qui-youth-superheros-heroup-highres.jpg?sfvrsn=0

https://pkrvworldwide.files.examplehost.com/2013/04/544477_432153653542694_970534114_n.jpg

Also my logo should be on it some where . I've attached a my logo.

Here is the text:
How to get organised and motivated this year.
1. Write stuff down
Write down things you need to do and when you plan to do them. Use digital calendars, to do apps and email lists – or pen and paper. Even if you are sure you will remember – get it out of your head and onto paper/your phone/laptop. You are more likely to get it done and feel less stressed.
2. Set up habits
If you do things in the same way, at the same time or after the same thing – then after a few weeks, it becomes much easier to get those things done. Set up a particular time, or place to do study tasks – or link them with another daily task. EG: art homework every Tuesday. Violin practice after breakfast.
3. Focus!
For 15-30 minutes at a time - totally focus on homework. Put your phone away, log out of chatterloop, close down other programs and really concentrate. Then have a break, send a text or whatever – and then go back to focussed study. Fifteen minutes of concentrated study gets more achieved than an hour of study switching back and forth between homework and other activities.
4. Just do something
No motivation? Just take a “bite”. Set a timer and just do 5 minutes. Or 15. Or read just the first two pages. Or the first problem on the worksheet. Something is better than nothing – and sometimes once you start, it’s easier to keep going.
5. Use rewards and consequences
Reward yourself when you do a hard task and use consequences when you don’t. Use food, fun activities, gaming and social time to motivate yourself – you get it when you do tasks, you don’t when you don’t. EG 15 minutes of clipstream when I finish this page. Tell other people your plans and you are more likely to stick to them.
6. Imagine the future
When you really can’t be find any motivation to do the things you need to do – take 30 seconds to think about what will happen in a week, month and year if you get on with it. What will happen then and how will that feel. And imagine what will happen in a week, month and year if you DON’T do those things – and how will that feel.

Good luck !
For free articles and one to one help with study skills, increasing motivation, coping with stress or tough times in senior school, go to tallowbrook.example.net.au
Tallow Brook Psychology and Education

```html
<!DOCTYPE html>
<html lang="en">
<head>
<meta charset="utf-8">
<title>How to get Organised and Motivated this Year</title>
<link rel="stylesheet" href="https://fonts.googleapis.com/css2?family=Fredoka:wght@600&family=Gochi+Hand&family=Patrick+Hand&family=Kalam:wght@700&display=swap">
<style>
:root{
  --teal:#3fb4c4;
  --teal-dark:#1f8897;
  --navy:#1d3f73;
  --orange:#f08a24;
  --orange-red:#e8602c;
  --lime:#b9cf3a;
  --green:#5c9b2f;
  --white:#ffffff;
  --paper:#fdfbf4;
  --ink:#24364f;
}
*{box-sizing:border-box;margin:0;padding:0}
html,body{width:849px;height:1200px;overflow:hidden}
body{background:var(--paper);font-family:"Patrick Hand",cursive;color:var(--ink);position:relative}
.header{position:absolute;left:0;top:0;width:849px;height:230px;background:var(--teal)}
.title{position:absolute;left:30px;top:16px;width:600px;font-weight:400;line-height:1}
.title .how{display:inline-block;background:var(--orange-red);color:var(--white);font-family:"Kalam",cursive;font-size:40px;padding:6px 20px 2px;border-radius:6px;transform:rotate(-2deg)}
.title .big{display:block;font-family:"Fredoka",sans-serif;font-weight:600;color:var(--navy);font-size:46px;margin-top:12px;white-space:nowrap}
.title .big small{font-family:"Kalam",cursive;color:var(--white);font-size:38px}
.title .year{display:block;margin-top:10px;padding-left:200px;white-space:nowrap}
.title .year small{font-family:"Kalam",cursive;color:var(--navy);font-size:32px;margin-right:10px}
.title .year b{display:inline-block;background:var(--orange-red);color:var(--white);font-family:"Fredoka",sans-serif;font-weight:600;font-size:40px;padding:4px 14px 2px;border-radius:6px}
.brand{position:absolute;right:24px;top:30px;display:flex;align-items:center;gap:10px;width:200px}
.brand .dot{flex:none;width:34px;height:34px;border-radius:50%;background:var(--green)}
.brand span{font-family:"Patrick Hand",cursive;color:var(--white);font-size:19px;line-height:1.1}
.tip{position:absolute;border-radius:14px;padding:66px 22px 16px;font-size:18.5px;line-height:1.2}
.tip h2{position:absolute;left:70px;right:10px;top:18px;font-family:"Gochi Hand",cursive;font-weight:400;font-size:31px;line-height:1;white-space:nowrap}
.tip .num{position:absolute;left:14px;top:12px;width:46px;height:46px;border-radius:50%;font-family:"Fredoka",sans-serif;font-weight:600;font-size:26px;display:flex;align-items:center;justify-content:center}
.tip-write{left:22px;top:258px;width:388px;height:318px;background:var(--orange);color:var(--white)}
.tip-write .num{background:var(--navy);color:var(--white)}
.tip-write h2{color:var(--navy)}
.tip-habits{left:432px;top:244px;width:396px;height:316px;background:var(--white);border:4px solid var(--orange-red)}
.tip-habits .num{background:var(--orange-red);color:var(--white)}
.tip-habits h2{color:var(--orange-red)}
.tip-focus{left:22px;top:598px;width:388px;height:324px;background:var(--teal);color:var(--white)}
.tip-focus .num{background:var(--white);color:var(--teal-dark)}
.tip-focus h2{color:var(--navy)}
.tip-start{left:432px;top:582px;width:396px;height:246px;background:var(--white);border:4px solid var(--teal)}
.tip-start .num{background:var(--teal);color:var(--white)}
.tip-start h2{color:var(--teal-dark)}
.tip-rewards{left:22px;top:944px;width:388px;height:236px;background:var(--lime);color:var(--ink);font-size:17.5px}
.tip-rewards .num{background:var(--green);color:var(--white)}
.tip-rewards h2{color:var(--green);font-size:24px;top:24px}
.tip-future{left:432px;top:852px;width:396px;height:328px;background:var(--orange-red);color:var(--white)}
.tip-future .num{background:var(--white);color:var(--orange-red)}
.tip-future h2{color:var(--white)}
.arrows{position:absolute;left:0;top:0;pointer-events:none}
</style>
</head>
<body>
<header class="header">
  <h1 class="title">
    <span class="how">How to get</span>
    <span class="big">ORGANISED <small>and</small> Motivated</span>
    <span class="year"><small>this</small><b>YEAR</b></span>
  </h1>
  <div class="brand"><i class="dot"></i><span>Tallow Brook Psychology and Education</span></div>
</header>

<section class="tip tip-write">
  <span class="num">1</span><h2>Write stuff down</h2>
  <p>Write down things you need to do and when you plan to do them. Use digital calendars, to do apps and email lists – or pen and paper. Even if you are sure you will remember – get it out of your head and onto paper/your phone/laptop. You are more likely to get it done and feel less stressed.</p>
</section>

<section class="tip tip-habits">
  <span class="num">2</span><h2>Set up habits</h2>
  <p>If you do things in the same way, at the same time or after the same thing – then after a few weeks, it becomes much easier to get those things done. Set up a particular time, or place to do study tasks – or link them with another daily task. EG: art homework every Tuesday. Violin practice after breakfast.</p>
</section>

<section class="tip tip-focus">
  <span class="num">3</span><h2>Focus!</h2>
  <p>For 15-30 minutes at a time - totally focus on homework. Put your phone away, log out of chatterloop, close down other programs and really concentrate. Then have a break, send a text or whatever – and then go back to focussed study. Fifteen minutes of concentrated study gets more achieved than an hour of study switching back and forth between homework and other activities.</p>
</section>

<section class="tip tip-start">
  <span class="num">4</span><h2>Just do something</h2>
  <p>No motivation? Just take a “bite”. Set a timer and just do 5 minutes. Or 15. Or read just the first two pages. Or the first problem on the worksheet. Something is better than nothing – and sometimes once you start, it’s easier to keep going.</p>
</section>

<section class="tip tip-rewards">
  <span class="num">5</span><h2>Use rewards and consequences</h2>
  <p>Reward yourself when you do a hard task and use consequences when you don’t. Use food, fun activities, gaming and social time to motivate yourself – you get it when you do tasks, you don’t when you don’t. EG 15 minutes of clipstream when I finish this page. Tell other people your plans and you are more likely to stick to them.</p>
</section>

<section class="tip tip-future">
  <span class="num">6</span><h2>Imagine the future</h2>
  <p>When you really can’t be find any motivation to do the things you need to do – take 30 seconds to think about what will happen in a week, month and year if you get on with it. What will happen then and how will that feel. And imagine what will happen in a week, month and year if you DON’T do those things – and how will that feel.</p>
</section>

<svg class="arrows" width="849" height="1200" viewBox="0 0 849 1200" aria-hidden="true">
  <g fill="none" stroke="var(--navy)" stroke-width="4" stroke-linecap="round" stroke-linejoin="round">
    <path d="M418 590 Q430 610 418 630"/><path d="M412 616 L418 631 L428 620"/>
    <path d="M418 930 Q430 900 440 880"/><path d="M428 884 L441 879 L442 894"/>
  </g>
</svg>
</body>
</html>
```